Life Coach for Lawyers Business Card Design

Elegant, original, business card design for life coaching service for associate attorneys who work in big law and struggle with stress, overwhelm, and time management. Double sided design.

Target Market(s)

Women associate attorneys who work in big law and struggle with stress, overwhelm, and time management.

Industry/Entity Type

Life Coaching

Contact Information for Business Card

Marissa Pendrell
Life Coach
518.677.3941
calmbriefcounsel.net
marissa@calmbriefcounsel.net
@calmbriefcounsel (Instagram)

Font styles to use
Other font styles liked:
• Silver South font duo. See uploaded files.

Requirements
Must have
• Icons for phone, website, email, and Instagram instead of words. Specific colors used in my logo (171B2B, 421121, FFFFFF)
Nice to have
• Foil. Embossed. Feminine design.
Should not have
• Any colors other than those used in logo. See uploaded files.

```html
<!DOCTYPE html>
<html lang="en">
<head>
<meta charset="utf-8">
<title>Calm Brief Counsel — Business Card</title>
<link rel="stylesheet" href="https://fonts.googleapis.com/css2?family=Cormorant+Garamond:wght@500&family=Shadows+Into+Light&display=swap">
<style>
  :root {
    --stage: #251820;
    --card: #421121;
    --card-tint: #5a2236;
    --ink: #ffffff;
    --ink-soft: #f1e6ea;
  }
  * { margin: 0; padding: 0; box-sizing: border-box; }
  html, body { width: 1200px; height: 1036px; overflow: hidden; }
  body {
    background: var(--stage);
    display: flex;
    flex-direction: column;
    align-items: center;
    justify-content: center;
    gap: 64px;
    font-family: "Cormorant Garamond", Georgia, serif;
  }
  .card {
    width: 660px;
    height: 378px;
    background: var(--card);
    border-radius: 34px;
    position: relative;
    color: var(--ink);
  }
  /* Back side: quiet seal with the business name */
  .card--back { display: flex; align-items: center; justify-content: center; }
  .seal {
    width: 220px; height: 220px;
    border: 2px solid var(--card-tint);
    border-radius: 50%;
    display: flex; align-items: center; justify-content: center;
    text-align: center;
  }
  .seal__name {
    font-size: 26px; font-weight: 500; line-height: 1.15;
    letter-spacing: 3px; text-transform: uppercase;
    color: var(--card-tint);
  }
  /* Front side */
  .card--front {
    display: flex; flex-direction: column; align-items: center;
    padding-top: 66px;
  }
  .brand {
    font-size: 44px; font-weight: 500; letter-spacing: 4px;
    text-transform: uppercase; line-height: 1; text-align: center;
    color: var(--ink);
  }
  .person { margin-top: 34px; text-align: center; }
  .person__name {
    font-family: "Shadows Into Light", cursive;
    font-size: 36px; letter-spacing: 2px; text-transform: uppercase;
    line-height: 1;
  }
  .person__title {
    font-size: 15px; letter-spacing: 2px; text-transform: uppercase;
    color: var(--ink-soft); margin-top: 4px;
  }
  .contacts {
    position: absolute; left: 0; right: 0; bottom: 48px;
    display: flex; flex-direction: column; align-items: center; gap: 8px;
    font-size: 15px; letter-spacing: 1px; text-transform: uppercase;
    color: var(--ink-soft);
  }
  .contacts__row { display: flex; gap: 22px; }
  .contact { display: flex; align-items: center; gap: 6px; }
  .contact svg { width: 13px; height: 13px; flex: none; }
  .contact__square { width: 10px; height: 10px; background: var(--ink-soft); border-radius: 2px; }
</style>
</head>
<body>
  <section class="card card--back" aria-label="Card back">
    <div class="seal">
      <span class="seal__name">Calm<br>Brief<br>Counsel</span>
    </div>
  </section>

  <section class="card card--front" aria-label="Card front">
    <h1 class="brand">Calm Brief Counsel</h1>
    <div class="person">
      <p class="person__name">Marissa Pendrell</p>
      <p class="person__title">Life Coach</p>
    </div>
    <div class="contacts">
      <div class="contacts__row">
        <span class="contact">
          <svg viewBox="0 0 16 16" fill="currentColor" aria-hidden="true"><path d="M3.6 1.5 6 4l-1.3 1.8c.9 2 2.5 3.6 4.5 4.5L11 9l2.5 2.4-1.4 2.2C6.6 13.3 2.7 9.4 2.4 3.9z"/></svg>
          518.677.3941
        </span>
        <span class="contact">
          <svg viewBox="0 0 16 16" fill="none" stroke="currentColor" stroke-width="1.4" aria-hidden="true"><rect x="1.5" y="3.5" width="13" height="9"/><path d="M1.5 3.5 8 9l6.5-5.5"/></svg>
          marissa@calmbriefcounsel.net
        </span>
      </div>
      <div class="contacts__row">
        <span class="contact">
          <svg viewBox="0 0 16 16" fill="none" stroke="currentColor" stroke-width="1.3" aria-hidden="true"><circle cx="8" cy="8" r="6.3"/><ellipse cx="8" cy="8" rx="2.8" ry="6.3"/><path d="M1.7 8h12.6"/></svg>
          calmbriefcounsel.net
        </span>
        <span class="contact">
          <span class="contact__square" aria-hidden="true"></span>
          @calmbriefcounsel
        </span>
      </div>
    </div>
  </section>
</body>
</html>
```